Design for Pediatric Occupational Therapist who works with children with special needs

I need 2 x 2 sq business cards and post cards for my Pediatric Occupational Therapy business. We work with children with special needs and help them learn skills for daily living (eating, writing, dressing, etc). We're looking for a colorful design (not loud) that looks professional and helps it stand out from other cards. I want to avoid many of the standard designs that you see on Pella press which are used my many other Pediatric OT's. The design will be intended for business cards, post cards and hopefully can also be used on company letterhead. I'll upload a current copy of the logo we currently use on company letter head so you get an idea of the design we've been using to date. This image does not need to be used again, but serves more as a reference to the design used in the past. The winning designer will likely be hired to design a custom logo for letter head.

Target Market(s)

Families of children with special needs, pediatricians

Industry/Entity Type

Business

Contact Information for Business Card

I need a logo or design for 2 x 2 sq business cards and post cards for my Pediatric Occupational Therapy business. We work with children with special needs and help them learn skills for daily living (eating, writing, dressing, etc). We're looking for a colorful design (not loud) that looks professional and helps it stand out from other cards. I want to avoid many of the standard designs that you see on Pella press which are used my many other Pediatric OT's. The design will be intended for business cards, post cards and hopefully can also be used on company letterhead. I'll upload a current copy of the logo we currently use on company letter head so you get an idea of the design we've been using to date.

Font styles to use
Sans Serif

Requirements
Must have
• Area to include company name, address, phone, etc.
• Company name = Brightway Care Partners

```html
<!DOCTYPE html>
<html lang="en">
<head>
<meta charset="utf-8">
<title>Pediatric Therapy Square Business Card – Front and Back</title>
<link rel="stylesheet" href="https://fonts.googleapis.com/css2?family=Chewy&family=Source+Sans+3:wght@400&family=Arimo:wght@700&display=swap">
<style>
  :root {
    --backdrop: #000000;
    --card-teal: #15a49b;
    --card-teal-deep: #12978f;
    --title-mint: #b6e7e1;
    --text-white: #ffffff;
    --kids-red: #d9493f;
    --kids-yellow: #f2b630;
    --kids-blue: #3a8fd0;
    --kids-green: #4aa04a;
    --kids-pink: #c94a8c;
  }
  * { margin: 0; padding: 0; box-sizing: border-box; }
  html, body {
    width: 1200px;
    height: 999px;
    overflow: hidden;
    background: var(--backdrop);
  }
  .canvas {
    position: relative;
    width: 1200px;
    height: 999px;
  }
  .card {
    position: absolute;
    width: 560px;
    height: 560px;
    background: linear-gradient(180deg, var(--card-teal) 0%, var(--card-teal-deep) 100%);
  }
  .card--front {
    left: 30px;
    top: 226px;
    border-radius: 110px 0 100px 0;
  }
  .card--back {
    left: 616px;
    top: 228px;
    border-radius: 0 110px 0 100px;
  }
  .front-content {
    position: absolute;
    left: 0;
    top: 0;
    width: 556px;
    text-align: center;
    color: var(--text-white);
  }
  .company-name {
    position: absolute;
    left: 0;
    width: 100%;
    top: 68px;
    font-family: "Chewy", "Comic Sans MS", cursive;
    font-size: 64px;
    line-height: 64px;
    letter-spacing: 3px;
    color: var(--title-mint);
    font-weight: 400;
  }
  .person-name {
    position: absolute;
    left: 0;
    width: 100%;
    top: 237px;
    font-family: "Arimo", Arial, sans-serif;
    font-weight: 700;
    font-size: 33px;
    line-height: 40px;
  }
  .designation, .address, .contact {
    position: absolute;
    left: 0;
    width: 100%;
    font-family: "Source Sans 3", "Myriad Pro", sans-serif;
    font-size: 24px;
    line-height: 33px;
  }
  .designation { top: 281px; }
  .address { top: 334px; font-style: normal; }
  .contact { top: 417px; list-style: none; }
  .kids-illustration {
    position: absolute;
    left: 42px;
    top: 236px;
    width: 478px;
    height: 96px;
    border-radius: 12px;
    background: linear-gradient(90deg,
      var(--kids-green) 0%, var(--kids-red) 14%, var(--kids-blue) 28%,
      var(--kids-pink) 42%, var(--kids-yellow) 56%, var(--kids-green) 68%,
      var(--kids-blue) 80%, var(--kids-pink) 90%, var(--kids-blue) 100%);
    opacity: 0.75;
  }
</style>
</head>
<body>
  <main class="canvas">
    <section class="card card--front" aria-label="Business card front">
      <div class="front-content">
        <h1 class="company-name">COMPANY<br>NAME</h1>
        <p class="person-name">Person Name</p>
        <p class="designation">Designation</p>
        <address class="address">suit # 00, Lorem ipsum<br>Lorem Lorem ipsum</address>
        <ul class="contact">
          <li>Tel: 000-000-0000</li>
          <li>Email: abcde@abcdef.com</li>
          <li>Web: www.abcdef.com</li>
        </ul>
      </div>
    </section>
    <section class="card card--back" aria-label="Business card back">
      <div class="kids-illustration" role="img" aria-label="Illustration of a row of nine colourful cartoon children holding hands"></div>
    </section>
  </main>
</body>
</html>
```